Ground breaking athletic gear company needs a kick ass business card

We are an American start up athletic gear company that uses a medically proven biohack to boost athletic performance. Heat kills strength and endurance. Our gear helps athletes manage heat better and ultimatley can improve them by up to 10% instantly. Nothing like it out there! Launching this summer.
We are looking for a modern, minimalist design that captures a sporty edge. Check out www.vanteluxgear.com, @vanteluxgear on pictorama for more ideas.

Target Market(s)

25-35 year olds, male and female athletes, vortexlift athletes, competitive runners

Industry/Entity Type

Business

Contact Information for Business Card

Derek Hollins
Founder
derekh@vanteluxgear.com
www.VanteluxGear.com
+1 (555) 014-2286

Font styles to use
Sans Serif

Requirements
Must have
• Logo and icon
• All contact information
• derekh@vanteluxgear.com
• +1 (555) 019-4431 M
• +1 (555) 014-2286
Nice to have
• Tag line : "Chill & Prevail"

```html
<!DOCTYPE html>
<html lang="en">
<head>
<meta charset="utf-8">
<title>Vantelux Gear – Business Card</title>
<link href="https://fonts.googleapis.com/css2?family=Open+Sans:wght@300;400;700&display=swap" rel="stylesheet">
<style>
  :root {
    --bg: #e9e7e3;
    --card-black: #0a0a0a;
    --card-white: #ffffff;
    --band-grey: #a9a9a9;
    --ink: #1a1a1a;
    --ink-soft: #8a8a8a;
    --ink-light: #ffffff;
  }
  * { box-sizing: border-box; margin: 0; padding: 0; }
  html, body {
    width: 1200px; height: 950px; overflow: hidden;
    background: var(--bg);
    font-family: "Open Sans", Arial, sans-serif;
  }
  .canvas { position: relative; width: 1200px; height: 950px; }
  .card {
    position: absolute; left: 220px;
    width: 760px; height: 434px;
    border-radius: 22px; overflow: hidden;
    box-shadow: 0 10px 30px rgba(0,0,0,.18);
  }
  .card--front { top: 36px; background: var(--card-white); }
  .card--back { top: 494px; background: var(--card-black); }

  .front-shape { position: absolute; inset: 0; }

  .identity {
    position: absolute; right: 240px; top: 62px; text-align: right;
  }
  .identity__name { font-size: 30px; font-weight: 700; color: var(--ink); letter-spacing: -.3px; }
  .identity__role { font-size: 18px; font-weight: 400; color: var(--ink-soft); margin-top: 2px; }

  .brand {
    position: absolute; left: 44px; bottom: 58px;
    display: flex; align-items: center; gap: 12px;
  }
  .brand__mark { width: 18px; height: 18px; border: 2px solid var(--ink); }
  .brand__name { font-size: 22px; font-weight: 400; color: var(--ink); letter-spacing: 3px; text-transform: uppercase; }

  .contact {
    position: absolute; left: 370px; bottom: 44px;
    list-style: none; display: flex; flex-direction: column; gap: 8px;
  }
  .contact__item { display: flex; align-items: center; gap: 12px; font-size: 18px; color: var(--ink); }
  .contact__icon { width: 18px; height: 18px; flex: none; }

  .tagline {
    position: absolute; left: 70px; top: 0; bottom: 0;
    display: flex; flex-direction: column; align-items: center; justify-content: center;
    gap: 16px;
  }
  .tagline__rule { width: 1px; height: 80px; background: var(--ink-light); }
  .tagline__text {
    writing-mode: vertical-rl; transform: rotate(180deg);
    color: var(--ink-light); font-size: 15px; font-weight: 300;
    letter-spacing: 4px; text-transform: uppercase; white-space: nowrap;
  }
  .back-brand {
    position: absolute; left: 200px; right: 60px; top: 0; bottom: 0;
    display: flex; align-items: center; justify-content: center;
    color: var(--ink-light); font-size: 44px; font-weight: 300;
    letter-spacing: 8px; text-transform: uppercase;
  }
</style>
</head>
<body>
<main class="canvas">

  <section class="card card--front" aria-label="Card front">
    <svg class="front-shape" width="760" height="434" viewBox="0 0 760 434" aria-hidden="true">
      <rect width="760" height="434" fill="var(--card-black)"/>
      <ellipse cx="250" cy="360" rx="450" ry="470" fill="var(--band-grey)"/>
      <ellipse cx="220" cy="370" rx="430" ry="470" fill="var(--card-white)"/>
    </svg>

    <div class="identity">
      <p class="identity__name">Derek Hollins</p>
      <p class="identity__role">Founder</p>
    </div>

    <div class="brand">
      <span class="brand__mark"></span>
      <span class="brand__name">Vantelux Gear</span>
    </div>

    <ul class="contact">
      <li class="contact__item">
        <svg class="contact__icon" viewBox="0 0 18 18" aria-hidden="true"><rect x="4" y="1" width="10" height="16" rx="2" fill="none" stroke="var(--ink)" stroke-width="2"/></svg>
        +1 (555) 014-2286
      </li>
      <li class="contact__item">
        <svg class="contact__icon" viewBox="0 0 18 18" aria-hidden="true"><rect x="1" y="3" width="16" height="12" fill="var(--ink)"/><path d="M1 3 L9 10 L17 3" fill="none" stroke="var(--card-white)" stroke-width="1.5"/></svg>
        derekh@vanteluxgear.com
      </li>
      <li class="contact__item">
        <svg class="contact__icon" viewBox="0 0 18 18" aria-hidden="true"><circle cx="9" cy="9" r="8" fill="var(--ink)"/></svg>
        www.VanteluxGear.com
      </li>
    </ul>
  </section>

  <section class="card card--back" aria-label="Card back">
    <div class="tagline">
      <span class="tagline__rule"></span>
      <span class="tagline__text">Chill &amp; Prevail</span>
      <span class="tagline__rule"></span>
    </div>
    <div class="back-brand">Vantelux Gear</div>
  </section>

</main>
</body>
</html>
```